Web Design Project

I am looking for a simple website to promote my business called Maltby Fennick Consulting. We provide consulting and implementation services for finance and supply chain processes and systems.

We want to project a professional but innovative image. I have attached a copy of our logo. It is not necessary to stick with the colours in the logo - we encourage you to experiment with the colours and even to change the colours of the logo to fit with your design. Although, on the front page we would like to have the logo with its original colours.

Required sections:
About
What we do
Clients
Contact
Updates

Target Market(s)

Medium to large companies including multi-nationals in all industries.

Industry/Entity Type

Finance

Requirements
Must have
• Required sections:
About
What we do
Clients
Contact

Files

```html
<!DOCTYPE html>
<html lang="en">
<head>
<meta charset="utf-8">
<title>Maltby Fennick Consulting</title>
<link href="https://fonts.googleapis.com/css2?family=Arimo:wght@400;700&display=swap" rel="stylesheet">
<style>
:root{
  --page:#f3f3f3;
  --blue:#0a5cad;
  --green:#9bb20e;
  --ink:#111;
  --muted:#8a8a8a;
  --body:#6e6e6e;
  --rule:#d8d8d8;
  --strip:#e3e3e3;
  --footer:#262626;
  --footer-text:#c9c9c9;
}
*{margin:0;padding:0;box-sizing:border-box}
html,body{width:1200px;height:1192px;overflow:hidden}
body{background:var(--page);font-family:"Arimo",Arial,sans-serif;color:var(--ink);position:relative}
.abs{position:absolute}

/* header */
.site-header{position:absolute;left:0;top:0;width:1200px;height:132px;border-bottom:4px solid var(--green)}
.brand{left:157px;top:84px;color:var(--blue);font-weight:700;line-height:1.15}
.brand-name{font-size:17px;letter-spacing:.5px}
.brand-sub{font-size:11px;letter-spacing:1px}
.brand-mark{position:absolute;left:22px;top:-64px;width:56px;height:56px;border-radius:50%;background:var(--green)}
.phone{right:165px;top:30px;color:var(--blue);font-weight:700;font-size:17px;display:flex;align-items:center;gap:6px}
.main-nav{right:161px;top:63px;display:flex;align-items:center}
.main-nav a{font-size:14px;font-weight:700;color:#222;text-decoration:none;padding:0 24px;border-left:1px solid var(--rule);line-height:22px}
.main-nav a.active{background:var(--blue);color:#fff;border-radius:3px;padding:0 20px;line-height:38px;border:0;margin-right:1px}
.main-nav a.active+a{border-left:0}

/* hero */
.hero{left:0;top:136px;width:1200px;height:418px}
.hero-photo{position:absolute;inset:0;background:linear-gradient(120deg,#f4f4f6 0%,#e8e9ee 45%,#cfd2d6 70%,#9fa3a7 85%,#2a2a2a 100%)}
.hero-title{left:157px;top:141px;width:432px;height:55px;background:var(--green);color:#fff;font-weight:700;font-size:28px;line-height:55px;padding-left:16px}
.hero-sub{left:157px;top:204px;width:329px;height:42px;background:var(--blue);color:#fff;font-weight:700;font-size:22px;line-height:42px;padding-left:18px}
.slider-dots{left:550px;top:370px;display:flex;gap:6px}
.slider-dots span{width:28px;height:28px;border-radius:50%;background:#fff;border:1px solid #c8c8c8;display:flex;align-items:center;justify-content:center}
.slider-dots span::after{content:"";width:16px;height:16px;border-radius:50%;background:var(--blue)}

/* services */
.service{top:577px;width:280px;text-align:center}
.service-icon{width:60px;height:60px;border-radius:50%;background:var(--blue);margin:0 auto;display:flex;align-items:center;justify-content:center}
.service h3{font-size:17px;margin-top:18px;letter-spacing:.3px}
.service p{font-size:13px;line-height:18.5px;color:var(--muted);margin-top:12px}
.btn{display:inline-block;background:var(--green);color:#fff;font-size:14px;line-height:33px;width:103px;border-radius:2px;text-decoration:none;margin-top:13px}

.divider{left:157px;top:808px;width:886px;height:1px;background:var(--rule)}

/* who we are */
.section-title{font-size:16px;font-weight:700;letter-spacing:.3px}
.about{left:157px;top:838px;width:582px}
.about p{font-size:12.6px;line-height:16.7px;color:var(--body);margin-top:12px}
.arrows{left:686px;top:933px;display:flex;gap:5px}
.arrows span{width:23px;height:23px;background:var(--green);display:flex;align-items:center;justify-content:center}
.clients{left:157px;top:962px;width:581px;height:101px;background:var(--strip);display:flex;align-items:center}
.client{flex:1;height:66px;display:flex;align-items:center;justify-content:center;gap:6px;border-left:1px solid #cfcfcf;font-weight:700;font-size:20px;color:#2b2b2b}
.client:first-child{border-left:0;font-weight:400;font-size:13px;color:#555}
.client .dot{width:30px;height:30px;border-radius:50%;background:#8d8d8d}

.team{left:766px;top:838px;width:277px}
.team-photo{position:relative;margin-top:12px;height:125px;background:linear-gradient(90deg,#d9d4cf,#eef0f2 40%,#b9c0c8 75%,#e6e3e0)}
.team-photo .btn{position:absolute;right:0;bottom:0;margin:0;width:102px;line-height:34px;text-align:center;border-radius:0}
.team p{font-size:12.6px;line-height:16.7px;color:var(--body);margin-top:8px}

/* footer */
.site-footer{left:0;top:1099px;width:1200px;height:93px;background:var(--footer);color:var(--footer-text);font-size:12px}
.footer-nav{position:absolute;left:155px;top:20px;display:flex}
.footer-nav a{color:var(--footer-text);text-decoration:none}
.footer-nav span{margin:0 14px}
.copyright{position:absolute;right:155px;top:20px}
</style>
</head>
<body>

<header class="site-header">
  <div class="abs brand">
    <span class="brand-mark"></span>
    <div class="brand-name">MALTBY FENNICK</div>
    <div class="brand-sub">CONSULTING LIMITED</div>
  </div>
  <div class="abs phone">
    <svg width="26" height="18" viewBox="0 0 26 18" aria-hidden="true"><path d="M2 6c0-4 22-4 22 0v2h-6V6c-3-1-7-1-10 0v2H2z" fill="#0a5cad"/><path d="M7 8h12l3 9H4z" fill="#0a5cad"/><circle cx="13" cy="12.5" r="2.5" fill="#fff"/></svg>
    <span>: 5550-123-456</span>
  </div>
  <nav class="abs main-nav">
    <a class="active" href="#">HOME</a>
    <a href="#">ABOUT</a>
    <a href="#">WHAT WE DO</a>
    <a href="#">CLIENTS</a>
    <a href="#" style="padding-right:0">CONTACT</a>
  </nav>
</header>

<section class="abs hero">
  <div class="hero-photo" role="img" aria-label="Photo of a printed bar chart under a magnifying glass"></div>
  <h1 class="abs hero-title">BUILDING YOUR BUSINESS</h1>
  <h2 class="abs hero-sub">GROWTH &amp; PROSPERITY</h2>
  <div class="abs slider-dots"><span></span><span></span><span></span></div>
</section>

<section class="abs service" style="left:155px">
  <div class="service-icon">
    <svg width="40" height="40" viewBox="0 0 40 40" aria-hidden="true"><circle cx="20" cy="20" r="16" fill="none" stroke="#fff" stroke-width="3"/><circle cx="20" cy="20" r="11" fill="#fff"/><text x="20" y="26" text-anchor="middle" font-family="Arimo,Arial,sans-serif" font-weight="700" font-size="17" fill="#0a5cad">$</text></svg>
  </div>
  <h3>FINANACIAL CONSULTING</h3>
  <p>Lorem Ipsum is simply dummy text of the printing and typesetting industry. Lorem Ipsum has been the industry's standard dummy</p>
  <a class="btn" href="#">Read More</a>
</section>
<section class="abs service" style="left:460px">
  <div class="service-icon">
    <svg width="36" height="36" viewBox="0 0 36 36" aria-hidden="true"><circle cx="17" cy="11" r="7" fill="#fff"/><path d="M4 30c0-8 6-11 13-11s11 3 11 7H34v6H4z" fill="#fff"/></svg>
  </div>
  <h3>MARKET ASSESSMENT</h3>
  <p>Lorem Ipsum is simply dummy text of the printing and typesetting industry. Lorem Ipsum has been the industry's standard dummy</p>
  <a class="btn" href="#">Read More</a>
</section>
<section class="abs service" style="left:765px">
  <div class="service-icon">
    <svg width="32" height="36" viewBox="0 0 32 36" aria-hidden="true"><ellipse cx="16" cy="11" rx="7" ry="9" fill="#fff"/><path d="M2 34c0-9 6-12 14-12s14 3 14 12z" fill="#fff"/></svg>
  </div>
  <h3>REGULATORY SUPPORT</h3>
  <p>Lorem Ipsum is simply dummy text of the printing and typesetting industry. Lorem Ipsum has been the industry's standard dummy</p>
  <a class="btn" href="#">Read More</a>
</section>

<div class="abs divider"></div>

<section class="abs about">
  <h2 class="section-title">WHO WE ARE</h2>
  <p>Lorem Ipsum is simply dummy text of the printing and typesetting industry. Lorem Ipsum has been the industry's standard dummy text ever since the 1500s, when an unknown printer took a galley of type and scrambled it to make a type specimen book. It has survived not only five centuries, but also the leap into electronic typesetting, remaining essentially unchanged. It was</p>
</section>
<div class="abs arrows">
  <span><svg width="10" height="12" viewBox="0 0 10 12" aria-hidden="true"><path d="M7 1L2 6l5 5" fill="none" stroke="#fff" stroke-width="2.5"/></svg></span>
  <span><svg width="10" height="12" viewBox="0 0 10 12" aria-hidden="true"><path d="M3 1l5 5-5 5" fill="none" stroke="#fff" stroke-width="2.5"/></svg></span>
</div>
<div class="abs clients">
  <div class="client"><span class="dot"></span>Corvel Hart</div>
  <div class="client">tallyra</div>
  <div class="client">brantwell</div>
  <div class="client">tallyra</div>
</div>

<section class="abs team">
  <h2 class="section-title">WHO WE ARE</h2>
  <div class="team-photo" role="img" aria-label="Photo of business people shaking hands at a meeting table">
    <a class="btn" href="#">Read More</a>
  </div>
  <p>Lorem Ipsum is simply dummy text of the printing and typesetting industry. Lorem Ipsum has been the industry's standard dummy text ever since the 1500s, when an unknown printer</p>
</section>

<footer class="abs site-footer">
  <nav class="footer-nav">
    <a href="#">Home</a><span>|</span><a href="#">About</a><span>|</span><a href="#">What we do</a><span>|</span><a href="#">Clients</a><span>|</span><a href="#">Contact</a>
  </nav>
  <div class="copyright">Maltby Fennick © 2013. All rights Reserved</div>
</footer>

</body>
</html>
```